Hadley's Groundwork Crew needs a logo/business cards.

i've just started a new Labouring Business, Called Hadley's Groundwork Crew, I provide high quality labouring servicing to local Builders and Tradesmen.
I'd like my business cards to reflect the hard work and dedication I put into my business.
I'd like to see Burnt Orange and blacks in the cards and logo.
I want my cards to catch peoples eye as there is A lot of dull business cards in my industry.

Target Market(s)

Builders and other tradesmen

Contact Information for Business Card

Hadley's Groundwork Crew

Font styles to use
Sans Serif

Colors
f78f20
ffc214
000000
ffffff

Requirements
Must have
• My name : Tom Hadley
• My Number: 0457962381
• Email Address : hadleygroundworkcrew@mailbarn.net
• A Sharp and Professional Design
Nice to have
• A unique design that separates my Cards from others,
• As I try to provide unique service to my clients I'd love my cards/logo to reflect this.

```html
<!DOCTYPE html>
<html lang="en">
<head>
<meta charset="utf-8">
<title>Hadley's Groundwork Crew – Business Card</title>
<link rel="stylesheet" href="https://fonts.googleapis.com/css2?family=Lato:wght@700;900&display=swap">
<style>
  :root {
    --card-orange: #f0a145;
    --ink: #231f20;
    --accent-yellow: #fbbf2e;
    --card-w: 1200px;
    --card-h: 686px;
  }
  * { margin: 0; padding: 0; box-sizing: border-box; }
  html, body {
    width: var(--card-w);
    height: var(--card-h);
    overflow: hidden;
    background: var(--card-orange);
  }
  .card {
    position: relative;
    width: var(--card-w);
    height: var(--card-h);
    background: var(--card-orange);
    color: var(--ink);
    font-family: "Lato", sans-serif;
    text-align: center;
  }
  .brand {
    position: absolute;
    left: 0;
    top: 92px;
    width: 100%;
    display: flex;
    justify-content: center;
    align-items: center;
    gap: 34px;
  }
  .brand-dot {
    width: 84px;
    height: 84px;
    border-radius: 50%;
    background: var(--accent-yellow);
    flex: none;
  }
  .brand-name {
    font-weight: 900;
    text-transform: uppercase;
    color: var(--ink);
    line-height: 1;
    text-align: center;
  }
  .brand-name-main {
    display: block;
    font-size: 118px;
    letter-spacing: 2px;
  }
  .brand-name-sub {
    display: block;
    margin-top: 22px;
    font-size: 42px;
    letter-spacing: 4px;
  }
  .owner-name {
    position: absolute;
    left: 0;
    top: 410px;
    width: 100%;
    font-size: 68px;
    font-weight: 700;
    line-height: 80px;
    letter-spacing: 3px;
    text-transform: uppercase;
  }
  .contact {
    position: absolute;
    left: 0;
    top: 583px;
    width: 100%;
    font-style: normal;
    font-weight: 700;
  }
  .contact-phone {
    display: inline-block;
    font-size: 25px;
    line-height: 30px;
    letter-spacing: 1.5px;
    text-decoration: underline;
    text-underline-offset: 4px;
  }
  .contact-email {
    display: block;
    margin-top: 4px;
    font-size: 21px;
    line-height: 28px;
    letter-spacing: 0.5px;
  }
</style>
</head>
<body>
  <main class="card">
    <header class="brand">
      <span class="brand-dot" aria-hidden="true"></span>
      <h1 class="brand-name">
        <span class="brand-name-main">Hadley's</span>
        <span class="brand-name-sub">Groundwork Crew</span>
      </h1>
    </header>
    <p class="owner-name">Tom Hadley</p>
    <address class="contact">
      <span class="contact-phone">0457962381</span>
      <span class="contact-email">hadleygroundworkcrew@mailbarn.net</span>
    </address>
  </main>
</body>
</html>
```